Pebble Lane real estate investment company needs a poster design

We would like a poster design size 18 x 24.
Poster wording -
I WANT TO BUY YOUR ( finish with logo) logo uploaded
website- www.pebblelane-homes.example
phone # 555-217-8843 ( color red for the phone number)
we would like to see the poster on 2 different backgrounds
Yellow background
White background
horizontal

```html
<!DOCTYPE html>
<html lang="en">
<head>
<meta charset="UTF-8">
<title>Pebble Lane – I Want To Buy Your Home Poster</title>
<link rel="stylesheet" href="https://fonts.googleapis.com/css2?family=Montserrat:wght@400;500;800;900&display=swap">
<style>
  :root {
    --page-bg: #e6e6e6;
    --poster-yellow: #ecb81f;
    --ink: #0d0d0d;
    --accent-red: #e8232f;
  }
  html, body {
    margin: 0;
    padding: 0;
    width: 1200px;
    height: 1200px;
    overflow: hidden;
    background: var(--page-bg);
  }
  .canvas {
    position: relative;
    width: 1200px;
    height: 1200px;
  }
  .poster {
    position: absolute;
    left: 40px;
    top: 167px;
    width: 1120px;
    height: 866px;
    background: var(--poster-yellow);
    font-family: "Montserrat", sans-serif;
    color: var(--ink);
  }
  .poster-frame {
    position: absolute;
    left: 36px;
    top: 37px;
    right: 36px;
    bottom: 37px;
    border: 2px solid var(--ink);
  }
  .headline {
    position: absolute;
    left: 0;
    right: 0;
    top: 92px;
    display: flex;
    justify-content: center;
    align-items: baseline;
    gap: 18px;
    margin: 0;
    font-weight: 500;
    font-size: 52px;
    letter-spacing: 0.01em;
  }
  .headline-emphasis {
    display: inline-block;
    color: var(--accent-red);
    font-weight: 900;
    font-size: 180px;
    line-height: 1;
    letter-spacing: -0.01em;
    transform: rotate(-6deg) translateY(18px);
  }
  .brand-name {
    position: absolute;
    left: 0;
    right: 0;
    top: 430px;
    margin: 0;
    text-align: center;
    font-weight: 900;
    font-size: 104px;
    line-height: 1;
    letter-spacing: 0.005em;
  }
  .phone {
    position: absolute;
    left: 0;
    right: 0;
    top: 662px;
    margin: 0;
    text-align: center;
    color: var(--accent-red);
    font-weight: 800;
    font-size: 88px;
    line-height: 1;
  }
  .website {
    position: absolute;
    left: 50%;
    top: 811px;
    transform: translate(-50%, -50%);
    padding: 0 26px;
    background: var(--poster-yellow);
    font-weight: 400;
    font-size: 30px;
    letter-spacing: 0.06em;
    white-space: nowrap;
  }
</style>
</head>
<body>
  <main class="canvas">
    <section class="poster">
      <div class="poster-frame"></div>
      <h1 class="headline">
        <span>I WANT TO</span>
        <span class="headline-emphasis">BUY</span>
        <span>YOUR</span>
      </h1>
      <p class="brand-name">Pebble Lane</p>
      <p class="phone">555-217-8843</p>
      <p class="website">www.pebblelane-homes.example</p>
    </section>
  </main>
</body>
</html>
```